Lanterns Valley Foundation Web Design

The design we need is for a WordPress blog that will be our content platform. We are a registered 501(c)3 non-profit that focuses on financially supporting the treatment of cancer patients that have been told they have no hope and there is nothing the conventional medical system can do for them. Through this wesbite we want to both rasie awareness about the treatment options plus, raise funds for treating patients. The two primary target audiences of the site are...

1. Terminally ill patients and their families to let them know that there is an option other then hospice and that we are hear to support that option.

2. People looking to help donate to a worthwhile cause that resonates with them.

The website is https://lanternsvalleyfoundation.org/

See attached logo designs!!!

Target Market(s)

Cancer patients and their families

Industry/Entity Type

Foundation

Font styles to use
Sans Serif

Colors
ffffff
fbed22

Requirements
Must have
• I like this look of this site. It is clean, simple, helpful, soft. I like the flow of the pages.
• http://www.brightpathgiving.org/
• I like the design and flow but NOT the color or boldness
• https://tqsn-youth.org/
• I like this style for a donation page.
• https://www.healingscience.org/we-are-hsa/join-the-cause/donations/one-time-donation
• with the addition of a Would you like your employer to match? button.
Nice to have
• White black and gold - but soft
• Even possibly grayscale like the site I like.

```html
<!DOCTYPE html>
<html lang="en">
<head>
<meta charset="utf-8">
<title>Lanterns Valley Foundation</title>
<link href="https://fonts.googleapis.com/css2?family=Roboto:ital,wght@0,400;0,500;0,700;1,400&family=Source+Sans+3:wght@400;600;700&display=swap" rel="stylesheet">
<style>
  :root {
    --gold: #edc95b;
    --gold-deep: #c5a748;
    --ink: #2f2f2f;
    --text: #555555;
    --heading: #4a4a4a;
    --muted: #8a8a8a;
    --line: #d9d9d9;
    --dark: #2b2b2b;
    --white: #ffffff;
  }
  * { box-sizing: border-box; margin: 0; padding: 0; }
  html, body { width: 1200px; height: 3209px; overflow: hidden; background: var(--white); }
  body { position: relative; font-family: "Roboto", Arial, sans-serif; color: var(--text); }
  .abs { position: absolute; }

  /* header */
  .site-header { position: absolute; left: 0; top: 0; width: 1200px; height: 113px; background: var(--white); z-index: 3; }
  .brand { position: absolute; left: 75px; top: 28px; display: flex; align-items: center; gap: 12px; }
  .brand-mark { width: 22px; height: 22px; background: var(--gold); }
  .brand-name { font-family: "Source Sans 3", sans-serif; font-weight: 700; font-size: 19px; line-height: 22px; color: var(--ink); text-transform: uppercase; letter-spacing: .5px; }
  .main-nav { position: absolute; right: 75px; top: 37px; display: flex; gap: 0; }
  .main-nav a { font-family: "Source Sans 3", sans-serif; font-size: 19px; color: var(--ink); text-decoration: none; padding: 9px 11px; border: 1px solid transparent; line-height: 24px; }
  .main-nav a.is-active { border-color: var(--gold); }

  /* hero */
  .hero { position: absolute; left: 0; top: 113px; width: 1200px; height: 636px; clip-path: polygon(0 0, 100% 0, 100% 80%, 0 100%); }
  .hero-photo { position: absolute; inset: 0; background: linear-gradient(100deg, #e9edf2 0%, #d7dde6 18%, #f4f2ef 42%, #f7f8f8 65%, #dfe5ea 100%); }
  .hero-copy { position: absolute; left: 616px; top: 330px; }
  .hero-title { font-family: "Source Sans 3", sans-serif; font-weight: 700; font-size: 39px; line-height: 46px; color: var(--ink); }
  .hero-actions { display: flex; gap: 13px; margin-top: 20px; }
  .btn { display: inline-flex; align-items: center; justify-content: center; font-family: "Source Sans 3", sans-serif; font-size: 21px; color: var(--ink); background: var(--gold); text-transform: uppercase; }
  .hero-actions .btn { height: 51px; }

  /* about */
  .about { position: absolute; left: 0; top: 760px; width: 1200px; text-align: center; }
  .section-title { font-family: "Source Sans 3", sans-serif; font-weight: 700; font-size: 46px; color: var(--heading); line-height: 56px; }
  .about p { width: 740px; margin: 8px auto 0; font-size: 15.5px; line-height: 24px; color: var(--text); }
  .about p + p { margin-top: 14px; }
  .about .btn { width: 166px; height: 49px; margin-top: 12px; }

  /* services band */
  .services { position: absolute; left: 0; top: 1070px; width: 1200px; height: 524px; clip-path: polygon(0 12.2%, 100% 0, 100% 85.7%, 0 100%); }
  .services-photo { position: absolute; inset: 0; background: radial-gradient(ellipse at 50% 45%, #4a4440 0%, #34312f 45%, #262626 100%); }
  .service-card { position: absolute; top: 132px; width: 498px; height: 250px; border: 1px solid #b9b9b9; }
  .service-card.support { left: 77px; }
  .service-card.donate { left: 622px; }
  .service-icon { position: absolute; left: 19px; top: 19px; width: 242px; height: 208px; background: var(--gold); }
  .service-icon::after { content: ""; position: absolute; inset: 7px; border: 2px solid var(--ink); }
  .service-body { position: absolute; left: 272px; top: 32px; width: 210px; color: var(--white); }
  .service-body h3 { font-family: "Source Sans 3", sans-serif; font-weight: 600; font-size: 29px; line-height: 34px; }
  .service-body p { font-size: 14.5px; line-height: 25px; margin-top: 6px; }
  .btn-outline { display: flex; align-items: center; justify-content: center; width: 186px; height: 47px; margin-top: 22px; border: 1px solid #cfcfcf; color: var(--gold); font-family: "Source Sans 3", sans-serif; font-size: 19px; text-transform: uppercase; }

  /* testimonials */
  .quote-mark { position: absolute; font-family: Georgia, serif; font-size: 330px; line-height: 1; color: #e6e6e6; font-weight: 700; }
  .quote-open { left: 70px; top: 1540px; }
  .quote-close { left: 985px; top: 1735px; }
  .testimonials { position: absolute; left: 0; top: 1620px; width: 1200px; text-align: center; }
  .testimonials .author { font-size: 18px; color: var(--ink); margin-top: 8px; }
  .testimonials blockquote { width: 700px; margin: 6px auto 0; font-style: italic; font-size: 14.5px; line-height: 24px; color: var(--text); }
  .slider-arrow { position: absolute; top: 1728px; }
  .slider-arrow.prev { left: 78px; }
  .slider-arrow.next { left: 1098px; }

  /* contact */
  .contact { position: absolute; left: 0; top: 1855px; width: 1200px; height: 466px; background: var(--gold); clip-path: polygon(0 19.7%, 100% 0, 100% 84%, 0 100%); }
  .contact .section-title { position: absolute; left: 0; width: 1200px; top: 75px; text-align: center; color: var(--ink); }
  .field { position: absolute; background: var(--gold-deep); color: var(--white); font-size: 14px; padding: 10px 8px; }
  .field.name { left: 242px; top: 149px; width: 229px; height: 41px; }
  .field.email { left: 490px; top: 149px; width: 229px; height: 41px; }
  .field.phone { left: 736px; top: 149px; width: 229px; height: 41px; }
  .field.message { left: 242px; top: 207px; width: 723px; height: 81px; }
  .send { position: absolute; left: 242px; top: 308px; width: 723px; height: 42px; background: var(--white); color: var(--ink); font-family: "Source Sans 3", sans-serif; font-size: 21px; display: flex; align-items: center; justify-content: center; text-transform: uppercase; }

  /* news */
  .news-title { position: absolute; left: 0; top: 2333px; width: 1200px; text-align: center; }
  .news-card { position: absolute; top: 2400px; width: 334px; height: 329px; border: 1px solid var(--line); background: var(--white); }
  .news-card:nth-of-type(1) { left: 77px; }
  .news-card:nth-of-type(2) { left: 432px; }
  .news-card:nth-of-type(3) { left: 787px; }
  .news-photo { position: absolute; left: 19px; top: 19px; width: 294px; height: 186px; }
  .news-photo.study { background: linear-gradient(120deg, #6b5a4a, #b49c82 50%, #8b7c6e); }
  .news-photo.ward { background: linear-gradient(110deg, #dfe6ee, #c7d4e2 45%, #f2f2f2); }
  .news-photo.ribbon { background: linear-gradient(120deg, #e7d7cf, #f4ece8 50%, #d8c3b8); }
  .news-meta { position: absolute; left: 19px; top: 165px; width: 294px; height: 40px; background: rgba(40,40,40,.72); color: var(--white); font-size: 17px; line-height: 40px; padding-left: 15px; }
  .news-card h4 { position: absolute; left: 25px; top: 222px; font-family: "Source Sans 3", sans-serif; font-weight: 400; font-size: 21px; color: var(--ink); }
  .news-card p { position: absolute; left: 25px; top: 264px; width: 285px; font-size: 14.5px; line-height: 26px; color: var(--text); }

  /* footer */
  .site-footer { position: absolute; left: 0; top: 2802px; width: 1200px; height: 407px; clip-path: polygon(0 15.7%, 100% 0, 100% 100%, 0 100%); }
  .footer-photo { position: absolute; inset: 0; background: linear-gradient(100deg, #2a2828, #3a3433 45%, #2b2a2a 100%); }
  .footer-brand { position: absolute; left: 96px; top: 185px; display: flex; align-items: center; gap: 14px; }
  .footer-brand .brand-mark { width: 30px; height: 30px; }
  .footer-brand .brand-name { color: var(--white); font-size: 26px; line-height: 30px; }
  .footer-col h5 { font-family: "Source Sans 3", sans-serif; font-weight: 600; font-size: 25px; color: var(--white); }
  .contact-info { position: absolute; left: 441px; top: 108px; width: 320px; }
  .contact-info ul { list-style: none; margin-top: 10px; }
  .contact-info li { position: relative; padding-left: 29px; font-size: 15px; line-height: 24px; color: var(--white); margin-bottom: 6px; }
  .contact-info svg { position: absolute; left: 0; top: 4px; }
  .newsletter { position: absolute; left: 802px; top: 108px; }
  .newsletter p { font-size: 15px; color: var(--white); margin-top: 8px; }
  .newsletter .email-field { width: 257px; height: 45px; background: var(--white); font-size: 14px; color: #555; padding: 13px 12px; margin-top: 9px; }
  .newsletter .btn { width: 163px; height: 45px; margin-top: 13px; font-weight: 600; font-size: 19px; }
  .footer-rule { position: absolute; left: 77px; top: 342px; width: 1046px; height: 1px; background: #5a5a5a; }
  .copyright { position: absolute; left: 77px; top: 367px; font-size: 14.5px; color: var(--white); }
  .copyright strong { color: var(--gold); font-weight: 700; }
  .social { position: absolute; right: 77px; top: 366px; display: flex; gap: 13px; }
  .social span { width: 18px; height: 18px; border-radius: 50%; background: #cfcfcf; }
</style>
</head>
<body>

<header class="site-header">
  <div class="brand"><span class="brand-mark"></span><span class="brand-name">Lanterns Valley<br>Foundation</span></div>
  <nav class="main-nav">
    <a class="is-active">Home</a><a>About</a><a>Donate</a><a>Support Hospitality</a><a>News</a><a>Contact</a>
  </nav>
</header>

<section class="hero">
  <div class="hero-photo" role="img" aria-label="Patient in a headscarf resting in a hospital bed by a bright window"></div>
  <div class="hero-copy">
    <h1 class="hero-title">financially supporting the<br>treatment of cancer patients</h1>
    <div class="hero-actions">
      <span class="btn" style="width:143px">Donate</span>
      <span class="btn" style="width:146px">Support</span>
    </div>
  </div>
</section>

<section class="about">
  <h2 class="section-title">About Us</h2>
  <p>Lorem Ipsum is simply dummy text of the printing and typesetting industry. Lorem Ipsum has been the industry's standard dummy text ever since the 1500s, when an unknown printer took a galley of type and scrambled it to make a type specimen book. It has survived not only five centuries, but also the leap into electronic typesetting, remaining essentially unchanged.</p>
  <p>It was popularised in the 1960s with the release of Letraset sheets containing Lorem Ipsum passages, and more recently with desktop publishing software like Aldus PageMaker including versions of Lorem Ipsum.</p>
  <span class="btn">Know More</span>
</section>

<section class="services">
  <div class="services-photo" role="img" aria-label="Dim photo of two hands clasped together"></div>
  <article class="service-card support">
    <div class="service-icon" role="img" aria-label="Icon of helping hands"></div>
    <div class="service-body">
      <h3>Support</h3>
      <p>Lorem Ipsum is simply dummy text of the printing and typesetting industry.</p>
      <span class="btn-outline">View Details</span>
    </div>
  </article>
  <article class="service-card donate">
    <div class="service-icon" role="img" aria-label="Icon of a hand giving a coin"></div>
    <div class="service-body">
      <h3>Donate</h3>
      <p>Lorem Ipsum is simply dummy text of the printing and typesetting industry.</p>
      <span class="btn-outline">View Details</span>
    </div>
  </article>
</section>

<span class="quote-mark quote-open">&ldquo;</span>
<span class="quote-mark quote-close">&rdquo;</span>
<section class="testimonials">
  <h2 class="section-title">Testimonials</h2>
  <p class="author">-Commentetor Name</p>
  <blockquote>Lorem Ipsum is simply dummy text of the printing and typesetting industry. Lorem Ipsum has been the industry's standard dummy text ever since the 1500s, when an unknown printer took a galley of type and scrambled it to make a type specimen book.</blockquote>
</section>
<svg class="slider-arrow prev" width="16" height="30" viewBox="0 0 16 30"><polyline points="14,2 2,15 14,28" fill="none" stroke="#edc95b" stroke-width="3"/></svg>
<svg class="slider-arrow next" width="16" height="30" viewBox="0 0 16 30"><polyline points="2,2 14,15 2,28" fill="none" stroke="#edc95b" stroke-width="3"/></svg>

<section class="contact">
  <h2 class="section-title">Contact Us</h2>
  <div class="field name">Name</div>
  <div class="field email">E-mail</div>
  <div class="field phone">Phone</div>
  <div class="field message">Mesage</div>
  <div class="send">Send</div>
</section>

<h2 class="section-title news-title">Latest News</h2>
<article class="news-card">
  <div class="news-photo study" role="img" aria-label="Woman reading documents at a table"></div>
  <div class="news-meta">20 March, 2017 / 17 Views</div>
  <h4>The blog title</h4>
  <p>Lorem Ipsum is simply dummy text of the printing and typesetting industry.</p>
</article>
<article class="news-card">
  <div class="news-photo ward" role="img" aria-label="Patient in a headscarf sitting in a hospital bed"></div>
  <div class="news-meta">20 March, 2017 / 17 Views</div>
  <h4>The blog title</h4>
  <p>Lorem Ipsum is simply dummy text of the printing and typesetting industry.</p>
</article>
<article class="news-card">
  <div class="news-photo ribbon" role="img" aria-label="Hands forming a heart around a pink awareness ribbon"></div>
  <div class="news-meta">20 March, 2017 / 17 Views</div>
  <h4>The blog title</h4>
  <p>Lorem Ipsum is simply dummy text of the printing and typesetting industry.</p>
</article>

<footer class="site-footer">
  <div class="footer-photo" role="img" aria-label="Dark photo of hands holding a small heart"></div>
  <div class="footer-brand"><span class="brand-mark"></span><span class="brand-name">Lanterns Valley<br>Foundation</span></div>
  <div class="footer-col contact-info">
    <h5>Contact Info</h5>
    <ul>
      <li><svg width="16" height="18" viewBox="0 0 16 18"><path d="M8 1a6 6 0 0 0-6 6c0 4.5 6 10 6 10s6-5.5 6-10a6 6 0 0 0-6-6z" fill="#edc95b"/><circle cx="8" cy="7" r="2.2" fill="#2b2b2b"/></svg>Lorem Ipsum is simply dummy text of the printing and typesetting.</li>
      <li><svg width="16" height="16" viewBox="0 0 16 16"><path d="M3 1l3 3-2 2c1 2 3 4 6 6l2-2 3 3-2 2C7 15 1 9 1 3z" fill="#edc95b"/></svg>123 456 7890</li>
      <li><svg width="17" height="13" viewBox="0 0 17 13"><rect x="1" y="1" width="15" height="11" fill="none" stroke="#edc95b" stroke-width="1.6"/><polyline points="1,1 8.5,7 16,1" fill="none" stroke="#edc95b" stroke-width="1.6"/></svg>info@lanternsvalley.org</li>
    </ul>
  </div>
  <div class="footer-col newsletter">
    <h5>Newsletter</h5>
    <p>Subscribe to Our Newsletter</p>
    <div class="email-field">Enter Your Email</div>
    <span class="btn">Subscribe</span>
  </div>
  <div class="footer-rule"></div>
  <p class="copyright">&copy;<strong>Lanterns Valley Foundation</strong>. 2017 - All Rights Reserved.</p>
  <div class="social"><span></span><span></span><span></span><span></span></div>
</footer>

</body>
</html>
```